Flyer-Design für mobiles Eiscafé / KM R7 Retro Style  / Die Frohe Kutsche
Zielgruppe
Die Frohe Kutsche ist ein mobiles Eiscafe, aus dem Kaffee, Eis und Crepes angeboten werden.
Cocktails werden ebenfalls angebnoten , stellen im Moment aber nicht das Hauptaugenmerk da, daher kann dies erst einmal vernachlässigt werden. Sollte daher erst einmal nicht erwähnt werden.
Unsere Zielgruppe sind sowohl Firmen (Firmenveranstaltungen, Jubiäen, Sommerfeste etc. ) als auch Privatveranstaltungen, wobei das Hauptaugenmerk auf Hochzeiten liegt, ebenfalls natürlch Geburtstage, als auch Veranstaltungen wie Street Food Festivals, Flohmärkte etc.
Aufgabenstellung
Gerne im DIN A4 Format, so dass es als PDF im Anhang mit versandt werden kann.
Es soll als Flyer ebenfalls als Handout durchgehen und soll an die Unternehmen der Stadt verteilt werden.
Textlich recht offen - sollte selbstverständlich die Unternehmensdaten beinhalten, ansonsten liegt das Haupaugenmerk auf einen hochwertigem Design, das die extravaganz der Dienstleistung hervorhebt.
Weniger Text ist meines erachtens mehr, wer die Kontaktdaten einsehen möchte, der findet Sie auf dem Flyer, auch wenn Sie klein sind.
Gerne mit Tafeloptik, das passt zur Tafel am Kasti.
Stellt euch vor, Ihr würdet ein Hochzeitspaar ansprechen, das ist fein gekleidet, alle Personen sind Schick bei der Veranstaltung, dazu sollte der Flyer passen.
Im Mittelpunkt soll der Kasti stehen (Frostina), dann der Eismann und Barista - Gerd und gemeinsam sind Sie
'Die Frohe Kutsche' (on Tour).

```html
<!DOCTYPE html>
<html lang="de">
<head>
<meta charset="utf-8">
<title>Die Frohe Kutsche – Flyer Vorder- und Rückseite</title>
<link href="https://fonts.googleapis.com/css2?family=Rokkitt:wght@400&family=Yellowtail&family=Rubik:wght@400;700&family=Pathway+Gothic+One&display=swap" rel="stylesheet">
<style>
  :root{
    --page:#e4e4e2;
    --board-dark:#161616;
    --board-mid:#2e2e2e;
    --chalk:#f4f4f2;
    --sky:#5aaedb;
    --band:#3aa6d6;
    --chalk-line:rgba(244,244,242,.85);
    --photo-blue:#4aa9cf;
  }
  *{margin:0;padding:0;box-sizing:border-box}
  html,body{width:1200px;height:1200px;overflow:hidden;background:var(--page)}
  .canvas{position:relative;width:1200px;height:1200px}
  .flyer{
    position:absolute;width:493px;height:697px;overflow:hidden;
    background:radial-gradient(ellipse at 45% 35%,var(--board-mid) 0%,#222 45%,var(--board-dark) 100%);
    box-shadow:0 3px 10px rgba(0,0,0,.3);
  }
  .flyer--front{left:70px;top:248px}
  .flyer--back{left:629px;top:247px}
  .abs{position:absolute}
  .center{left:0;right:0;text-align:center}
  .tagline{font-family:"Rokkitt",serif;color:var(--sky);font-size:21px;letter-spacing:5px;top:22px}
  .rule{height:1.5px;background:var(--chalk-line);top:70px;left:81px;width:335px}
  .ornament{background:rgba(244,244,242,.18);border-radius:8px;height:14px}
  .brand{font-family:"Rokkitt",serif;color:var(--chalk);font-size:22px;line-height:24px;letter-spacing:2px}
  .brand-dot{width:10px;height:10px;border-radius:50%;background:var(--chalk);margin:0 auto 6px}
  .script{font-family:"Yellowtail",cursive;color:var(--chalk)}
  .headline{font-size:37px;line-height:1}
  .serif-blue{font-family:"Rokkitt",serif;color:var(--sky);letter-spacing:4px}
  .photo{background:linear-gradient(160deg,#8fd0ea,var(--photo-blue) 55%,#2f6f8c)}
  .frame{border:3px solid var(--chalk)}
  .contact-head{font-family:"Pathway Gothic One",sans-serif;color:var(--sky);font-size:13px}
  .small{font-family:"Rubik",sans-serif;color:var(--chalk);font-size:8px;line-height:10px;letter-spacing:.3px}
  .band{top:651px;left:22px;width:449px;height:18px}
  .band-text{font-family:"Rubik",sans-serif;color:var(--chalk);font-size:8px;line-height:18px;text-align:center}
  .band-text b{font-weight:700}
</style>
</head>
<body>
<div class="canvas">

  <!-- Vorderseite -->
  <section class="flyer flyer--front">
    <div class="abs center tagline">Kaffee | Eis | Crêpes</div>
    <div class="abs rule"></div>

    <div class="abs center" style="top:118px">
      <div class="brand-dot"></div>
      <div class="brand">Die Frohe<br>Kutsche</div>
    </div>

    <div class="abs script headline" style="left:73px;top:200px">Das Highlight für</div>
    <div class="abs script headline" style="left:128px;top:243px">Ihre Veranstaltung!</div>

    <div class="abs ornament" role="img" aria-label="Geschwungenes Kreide-Ornament" style="left:168px;top:305px;width:156px"></div>

    <div class="abs center serif-blue" style="top:323px;font-size:19px">Hochzeiten, Firmenevents,</div>
    <div class="abs center serif-blue" style="top:347px;font-size:19px">Kindergeburtstage …</div>
    <div class="abs center script" style="top:378px;font-size:14px">Ich freue mich auf Ihre Anfrage.</div>

    <div class="abs photo" role="img" aria-label="Foto: hellblauer Retro-Bus mit geöffneter Verkaufsklappe, Kreidetafel und Eisbecher-Aufsteller" style="left:0;top:414px;width:284px;height:201px;border-radius:40px 30px 18px 0"></div>

    <div class="abs photo frame" role="img" aria-label="Foto: Barista an der Espressomaschine im Bus" style="left:397px;top:407px;width:73px;height:85px;transform:rotate(4deg);background:linear-gradient(160deg,#c9c2b5,#6a6a6a 60%,#3a4b57)"></div>

    <div class="abs ornament" role="img" aria-label="Geschwungene Kreide-Klammer" style="left:323px;top:489px;width:118px;height:12px"></div>
    <div class="abs contact-head" style="left:336px;top:512px">Sprechen Sie mich an!</div>
    <div class="abs small" style="left:336px;top:530px">Gerd Kessler<br>Am Lindenhof 7<br>12345 Musterstadt</div>
    <div class="abs small" style="left:336px;top:569px">0151 / 20 48 73 65<br>info@frohe-kutsche.de</div>
    <div class="abs ornament" role="img" aria-label="Geschwungene Kreide-Klammer" style="left:323px;top:596px;width:118px;height:12px"></div>

    <div class="abs small" style="left:108px;top:606px;width:200px;font-size:7px;line-height:10px">„Frostina“ bringt Ihre Espressomaschine mit<br>&nbsp;&nbsp;&nbsp;und zaubert sowohl warme Kaffeespezialitäten,<br>sowie Eiskaffee und Café frappé.</div>

    <svg class="abs band" viewBox="0 0 449 18" aria-hidden="true">
      <polygon points="6,0 443,0 437,9 449,13 443,18 6,18 12,9 0,13" fill="var(--band)"/>
    </svg>
    <div class="abs band band-text">Weitere Informationen finden Sie unter <b>www.frohe-kutsche.de</b></div>
    <svg class="abs" style="left:34px;top:673px" width="425" height="6" aria-hidden="true">
      <path d="M0 3 Q4 0 8 3 T16 3 T24 3 T32 3 T40 3 T48 3 T56 3 T64 3 T72 3 T80 3 T88 3 T96 3 T104 3 T112 3 T120 3 T128 3 T136 3 T144 3 T152 3 T160 3 T168 3 T176 3 T184 3 T192 3 T200 3 T208 3 T216 3 T224 3 T232 3 T240 3 T248 3 T256 3 T264 3 T272 3 T280 3 T288 3 T296 3 T304 3 T312 3 T320 3 T328 3 T336 3 T344 3 T352 3 T360 3 T368 3 T376 3 T384 3 T392 3 T400 3 T408 3 T416 3 T424 3" fill="none" stroke="rgba(244,244,242,.5)" stroke-width="1"/>
    </svg>
  </section>

  <!-- Rückseite -->
  <section class="flyer flyer--back">
    <div class="abs center tagline">Kaffee | Eis | Crêpes</div>
    <div class="abs rule"></div>

    <div class="abs center" style="top:112px">
      <div class="brand-dot"></div>
      <div class="brand" style="font-size:18px;line-height:20px">Die Frohe<br>Kutsche</div>
    </div>

    <div class="abs ornament" role="img" aria-label="Geschwungenes Kreide-Ornament" style="left:167px;top:199px;width:156px"></div>

    <div class="abs serif-blue" style="left:151px;top:254px;font-size:22px">Kein</div>
    <div class="abs script" style="left:219px;top:228px;font-size:48px;line-height:1">Genuss</div>
    <div class="abs center serif-blue" style="top:292px;font-size:21px">ist vorübergehend.</div>
    <div class="abs center serif-blue" style="top:321px;font-size:21px">Den Eindruck,</div>
    <div class="abs center serif-blue" style="top:351px;font-size:21px">den er hinterlässt</div>
    <div class="abs center serif-blue" style="top:379px;font-size:21px">ist bleibend.</div>
    <div class="abs center script" style="top:414px;font-size:13px">Johanna Weidenfeld</div>

    <div class="abs ornament" role="img" aria-label="Geschwungenes Kreide-Ornament" style="left:167px;top:465px;width:156px"></div>

    <div class="abs photo frame" role="img" aria-label="Foto: hellblauer Bus bei Abendlicht" style="left:132px;top:508px;width:84px;height:63px;background:linear-gradient(170deg,#6d86a8,#3d6f96 55%,#3a3630)"></div>
    <div class="abs photo frame" role="img" aria-label="Foto: Gäste stehen unter Bäumen am Bus an" style="left:225px;top:508px;width:63px;height:63px;background:linear-gradient(170deg,#7f9a5a,#5c7a44 55%,#8a7a5e)"></div>
    <div class="abs photo frame" role="img" aria-label="Foto: Verkauf an der Klappe des Busses" style="left:297px;top:508px;width:62px;height:63px"></div>

    <div class="abs center contact-head" style="top:584px;font-size:12px">Ich freue mich auf Sie!</div>
    <div class="abs center small" style="top:603px">Ihr Gerd Kessler</div>

    <svg class="abs band" style="top:650px" viewBox="0 0 449 18" aria-hidden="true">
      <polygon points="6,0 443,0 437,9 449,13 443,18 6,18 12,9 0,13" fill="var(--band)"/>
    </svg>
    <div class="abs band band-text" style="top:650px">Weitere Informationen finden Sie unter <b>www.frohe-kutsche.de</b></div>
    <svg class="abs" style="left:34px;top:672px" width="425" height="6" aria-hidden="true">
      <path d="M0 3 Q4 0 8 3 T16 3 T24 3 T32 3 T40 3 T48 3 T56 3 T64 3 T72 3 T80 3 T88 3 T96 3 T104 3 T112 3 T120 3 T128 3 T136 3 T144 3 T152 3 T160 3 T168 3 T176 3 T184 3 T192 3 T200 3 T208 3 T216 3 T224 3 T232 3 T240 3 T248 3 T256 3 T264 3 T272 3 T280 3 T288 3 T296 3 T304 3 T312 3 T320 3 T328 3 T336 3 T344 3 T352 3 T360 3 T368 3 T376 3 T384 3 T392 3 T400 3 T408 3 T416 3 T424 3" fill="none" stroke="rgba(244,244,242,.5)" stroke-width="1"/>
    </svg>
  </section>

</div>
</body>
</html>
```